Letterhead for louvre roof company in NZ

I require a letter head design for a company called Slatwise Canopy.
I would like a footer to the letter head and possibly a water mark.
See attached logo.

```html
<!DOCTYPE html>
<html lang="en">
<head>
<meta charset="utf-8">
<title>Slatwise Canopy — Letterhead</title>
<link href="https://fonts.googleapis.com/css2?family=Lato:wght@400;700&display=swap" rel="stylesheet">
<style>
  :root {
    --backdrop: #e8e8e8;
    --paper: #ffffff;
    --ink: #3f3f3f;
    --ink-strong: #2a2a2a;
    --accent: #e8821e;
    --footer-bg: #0b0b0d;
    --footer-text: #f2f2f2;
    --footer-mark: #5a5a5a;
    --signature-tone: #d9d9d9;
  }
  * { box-sizing: border-box; margin: 0; padding: 0; }
  html, body {
    width: 1200px; height: 1200px; overflow: hidden;
    background: var(--backdrop);
    font-family: "Lato", sans-serif;
  }
  .letterhead {
    position: absolute; left: 174px; top: 0;
    width: 851px; height: 1200px;
    background: var(--paper);
    color: var(--ink);
  }
  .brand {
    position: absolute; left: 71px; top: 140px;
    display: flex; align-items: center; gap: 8px;
    color: var(--accent);
    font-weight: 700; font-size: 18px;
  }
  .brand-square { width: 12px; height: 12px; background: var(--accent); }
  .salutation, .closing {
    position: absolute; left: 71px;
    font-weight: 700; font-size: 16px; color: var(--ink-strong);
  }
  .salutation { top: 236px; }
  .closing { top: 666px; left: 73px; }
  .body-copy {
    position: absolute; left: 71px; width: 710px;
    font-size: 19.4px; line-height: 30.5px;
  }
  .body-copy.first { top: 279px; }
  .body-copy.second { top: 432px; }
  .signatory {
    position: absolute; left: 73px; top: 757px;
    font-weight: 700; font-size: 15px; line-height: 19px;
    letter-spacing: 3px; color: var(--ink-strong);
  }
  .signature {
    position: absolute; left: 72px; top: 806px;
    width: 158px; height: 76px;
    background: linear-gradient(90deg, var(--signature-tone), #efefef);
  }
  .footer-rule {
    position: absolute; left: 0; top: 1073px;
    width: 100%; height: 4px; background: var(--accent);
  }
  .footer {
    position: absolute; left: 0; top: 1083px;
    width: 100%; height: 117px;
    background: var(--footer-bg);
    color: var(--footer-text);
  }
  .contact-list {
    position: absolute; left: 71px; top: 17px;
    list-style: none; font-size: 13.5px;
  }
  .contact-list li { display: flex; align-items: center; gap: 5px; height: 17.5px; }
  .contact-list li.address { margin-top: 10px; }
  .contact-list svg { width: 10px; height: 10px; fill: var(--accent); flex: none; }
  .contact-list li.address svg { height: 14px; }
  .footer-brand {
    position: absolute; right: 56px; top: 74px;
    color: var(--footer-mark); font-weight: 700; font-size: 12px;
  }
</style>
</head>
<body>
  <main class="letterhead">
    <div class="brand"><span class="brand-square"></span>Slatwise Canopy</div>

    <p class="salutation">Valued customers,</p>

    <p class="body-copy first">A letterhead refers to the heading at the top of a sheet of letter paper. It usually consists of a name and an address, or a logo. This often appears in letters created by companies and individuals for communicating messages, whether it's within the team, business partners, or with clients.</p>

    <p class="body-copy second">Letterheads are important branding tools as well, as they are sent out to a wide audience. They can set the tone for messages while showcasing your company's expertise and professionalism. This makes it important for you to create a letterhead that captures your brand's identity while presenting important details. It helps to create a template that you can use for different occasions, from inter-office memos to customer correspondences.</p>

    <p class="closing">Valued customers,</p>

    <p class="signatory">MARA ELLISON<br>CO-OWNER</p>
    <div class="signature" role="img" aria-label="Handwritten signature of the co-owner"></div>

    <div class="footer-rule"></div>
    <footer class="footer">
      <ul class="contact-list">
        <li><svg viewBox="0 0 10 10"><path d="M1 3c0-1 1-2 4-2s4 1 4 2v1H7V3H3v1H1z M2 5h6l1 4H1z"/></svg>(123) 555 0199</li>
        <li><svg viewBox="0 0 10 10"><path d="M0 2h10v6H0z M0 2l5 3.5L10 2v1L5 6.5 0 3z" fill-rule="evenodd"/></svg>info@slatwisecanopy.com</li>
        <li><svg viewBox="0 0 10 10"><path d="M5 0a5 5 0 1 0 0 10A5 5 0 0 0 5 0zm0 1c.8 0 1.5 1.6 1.6 3.5H3.4C3.5 2.6 4.2 1 5 1zM1 5.5h1.9c.1 1.3.4 2.4.8 3.2A4 4 0 0 1 1 5.5zm0-1A4 4 0 0 1 3.7 1.3c-.4.8-.7 1.9-.8 3.2zm2.4 1h3.2C6.5 7.4 5.8 9 5 9s-1.5-1.6-1.6-3.5zm3.7 0H9a4 4 0 0 1-2.7 3.2c.4-.8.7-1.9.8-3.2zm0-1c-.1-1.3-.4-2.4-.8-3.2A4 4 0 0 1 9 4.5z"/></svg>www.slatwisecanopy.com</li>
        <li class="address"><svg viewBox="0 0 10 14"><path d="M5 0a5 5 0 0 0-5 5c0 3.5 5 9 5 9s5-5.5 5-9a5 5 0 0 0-5-5zm0 7a2 2 0 1 1 0-4 2 2 0 0 1 0 4z"/></svg>48 Harbour Crest Suite #7 Napier, HB 4110</li>
      </ul>
      <div class="footer-brand">Slatwise Canopy</div>
    </footer>
  </main>
</body>
</html>
```